BrivoMatex. Lantern for the Steady Growth. Business card

Professional business card for BrivoMatex (Lantern for the Steady Growth)
My rationale: Strategy-> Execution-> Results-> Value that lead to the BrivoMatex name: We put the Lantern for the Steady Growth.
We deliver value to our customers helping them at defining a good strategy (cyan arrow). 90% of well formulated strategies fail due to poor execution so we also consider strategical execution very important (green arrow). Due to the execution we obtain the results (blue arrow). Finally, the results provide feedback to redefine strategy, and the new strategy has to be executed and new results obtained providing new feedback and on and on. It's like a wheel that finally, must create corporate value: value for shareholders, staholders, employees, providers...-

Target Market(s)

CEOs and steering comitees , invewrnent funds

Industry/Entity Type

Business Consultant

Contact Information for Business Card

Tommaso Ferlini
CEO & Founder
tommaso.ferlini@brivomatex.example
Mobile: +34 611.205.938
www.brivomatex.example

Colors

Designer to choose colors to be used in the design.

Requirements
Nice to have
• Nice to hace the words: Strategy, execution, results
• Nice to vave the claim: Lantern for the Steady Growth
• The three colors should be shown:
• cyan for STRATEGY
• green for EXECUTION
• blue for RESULTS
Should not have
• Complete black background

```html
<!DOCTYPE html>
<html lang="en">
<head>
<meta charset="utf-8">
<title>BrivoMatex — Business Card</title>
<link rel="stylesheet" href="https://fonts.googleapis.com/css2?family=Roboto:wght@300;400;700&display=swap">
<style>
  :root {
    --canvas-bg: #2b2b2d;
    --card-bg: #1c1d20;
    --pattern-light: #34353a;
    --pattern-mid: #2a2b2f;
    --pattern-dark: #1b1c1f;
    --brand-blue: #1b3fb3;
    --accent-cyan: #1aa9e8;
    --text-blue: #1f4fc4;
    --rule-blue: #1d3f9e;
  }
  * { margin: 0; padding: 0; box-sizing: border-box; }
  html, body {
    width: 1200px; height: 1108px; overflow: hidden;
    background: var(--canvas-bg);
    font-family: "Roboto", Arial, sans-serif;
  }
  .canvas {
    position: relative; width: 1200px; height: 1108px;
    display: flex; justify-content: center; align-items: center; gap: 60px;
  }
  .card {
    width: 400px; height: 660px; border-radius: 22px;
    background: var(--card-bg);
    position: relative; overflow: hidden;
    box-shadow: 0 18px 40px rgba(0,0,0,.45);
  }
  .card-front {
    display: flex; flex-direction: column; align-items: center;
  }
  .brand-lockup {
    margin-top: 190px;
    display: flex; align-items: center; gap: 12px;
  }
  .brand-dot {
    width: 18px; height: 18px; border-radius: 50%;
    background: var(--brand-blue);
  }
  .brand-name {
    font-weight: 700; font-size: 52px; letter-spacing: -1px;
    color: var(--brand-blue);
  }
  .person { margin-top: 96px; text-align: center; }
  .person-name {
    font-weight: 700; font-size: 23px; color: var(--accent-cyan);
  }
  .person-role {
    margin-top: 3px; font-weight: 300; font-size: 15px; color: var(--rule-blue);
  }
  .contact-rule {
    margin-top: 14px; width: 300px;
    display: flex; align-items: center; gap: 8px;
  }
  .contact-rule::before, .contact-rule::after {
    content: ""; flex: 1; height: 1px; background: var(--rule-blue);
  }
  .icon { width: 28px; height: 28px; display: block; }
  .contact-list {
    margin-top: 14px; list-style: none; text-align: center;
    font-weight: 300; font-size: 16px; line-height: 1.6; color: var(--text-blue);
  }
  .card-back {
    background:
      radial-gradient(ellipse 70% 55% at 70% 15%, var(--pattern-light), transparent 70%),
      linear-gradient(165deg, var(--pattern-mid) 0%, var(--pattern-mid) 45%, var(--pattern-dark) 100%);
  }
  .back-lockup {
    position: absolute; right: 46px; top: 448px;
    display: flex; align-items: center; gap: 8px;
  }
  .back-dot {
    width: 12px; height: 12px; border-radius: 50%;
    background: var(--brand-blue);
  }
  .back-brand {
    font-weight: 700; font-size: 22px; color: var(--brand-blue);
  }
</style>
</head>
<body>
<main class="canvas">
  <section class="card card-front" aria-label="Business card front">
    <div class="brand-lockup">
      <span class="brand-dot" aria-hidden="true"></span>
      <h1 class="brand-name">BrivoMatex</h1>
    </div>
    <div class="person">
      <h2 class="person-name">Tommaso Ferlini</h2>
      <p class="person-role">CEO &amp; Founder</p>
    </div>
    <div class="contact-rule">
      <svg class="icon" viewBox="0 0 28 28" aria-label="Phone">
        <circle cx="14" cy="14" r="13" fill="var(--accent-cyan)"/>
        <path d="M9 8c1-1 2-1 3 0l1 2c.4.8 0 1.4-.6 1.8-.5.4-.6.9-.2 1.6.8 1.4 1.6 2.2 3 3 .7.4 1.2.3 1.6-.2.4-.6 1-1 1.8-.6l2 1c1 1 1 2 0 3-2 2-5 1-8-2s-4-7-2.6-9.6z" fill="#1c1d20"/>
      </svg>
      <svg class="icon" viewBox="0 0 28 28" aria-label="Email">
        <circle cx="14" cy="14" r="13" fill="var(--accent-cyan)"/>
        <rect x="7" y="9" width="14" height="10" rx="1" fill="#1c1d20"/>
        <path d="M7.5 9.5 14 15l6.5-5.5" stroke="var(--accent-cyan)" stroke-width="1.3" fill="none"/>
      </svg>
      <svg class="icon" viewBox="0 0 28 28" aria-label="Website">
        <circle cx="14" cy="14" r="13" fill="var(--accent-cyan)"/>
        <circle cx="14" cy="14" r="7" fill="none" stroke="#1c1d20" stroke-width="1.8"/>
        <ellipse cx="14" cy="14" rx="3" ry="7" fill="none" stroke="#1c1d20" stroke-width="1.5"/>
        <path d="M7 14h14" stroke="#1c1d20" stroke-width="1.5"/>
      </svg>
    </div>
    <ul class="contact-list">
      <li>+34 611.205.938</li>
      <li>www.brivomatex.example</li>
      <li>tommaso.ferlini@brivomatex.example</li>
    </ul>
  </section>

  <section class="card card-back" role="img" aria-label="Card back: repeating faint brand pattern in dark grey tones, fading toward the bottom, with the brand name">
    <div class="back-lockup">
      <span class="back-dot" aria-hidden="true"></span>
      <p class="back-brand">BrivoMatex</p>
    </div>
  </section>
</main>
</body>
</html>
```